Vaultrix Web Site

Hi Designers. Our web site at www.vaultrix.net.au needs a new look.

We do:

- off-site backup, every day, for vital data
- data recovery from crashed disks

We have an existing logo

Our colour is blue. Our image is about Trust and Competence

We are in Perth, Western Australia. Our photographs are local images.

We've been in business for fifteen years.

We have a second URL too: www.keep-our-records.com.au

Both URLs go to the same web site.

Would you like to take on this project?

Target Market(s)

Target market is small to medium business, with between 5 and 100 staff. Customers are mainly in Australia but can be anywhere. There are other providers who are cheaper- our point of difference is that we are highly professional and have been in the business for 15 years. personal attention is important to us- we promise Extreme Service.

Industry/Entity Type

Data Recovery

Requirements
Must have
• Our image is about Trust and Competence. Existing text from our web site can be used.
Should not have
• No moving Flash, no Flash intro

```html
<!DOCTYPE html>
<html lang="en">
<head>
<meta charset="utf-8">
<title>Vaultrix Computer Services</title>
<link rel="stylesheet" href="https://fonts.googleapis.com/css2?family=Arimo:ital,wght@0,400;0,700;1,700&display=swap">
<style>
:root{
  --navy:#0f3f6e;
  --blue:#124b80;
  --blue-light:#1d6aa8;
  --brand:#2b5a86;
  --brand-dark:#14375c;
  --teal:#1a6a9a;
  --ink:#111;
  --grey:#e9edf1;
  --white:#fff;
  --gold:#f2b21c;
}
*{margin:0;padding:0;box-sizing:border-box}
html,body{width:1200px;height:1019px;overflow:hidden}
body{font-family:"Arimo",Arial,sans-serif;color:var(--ink);background:var(--white);position:relative}
.abs{position:absolute}

.top-nav{left:0;top:0;width:1200px;height:52px;background:linear-gradient(#2a2a2a,#0b0b0b)}
.top-nav ul{list-style:none;display:flex;position:absolute;left:76px;top:14px;font-size:17px;color:#fff}
.top-nav li+li::before{content:"|";color:#888;margin:0 9px}
.top-nav .active-mark{left:86px;top:44px;width:0;height:0;border:8px solid transparent;border-bottom-color:#fff;border-top:0}

.masthead{left:0;top:52px;width:1200px;height:132px;background:linear-gradient(#fff,#f1f3f5)}
.brand-mark{left:76px;top:84px;width:84px;height:84px;background:var(--brand)}
.brand-name{left:238px;top:82px;font-size:50px;font-weight:700;color:var(--brand)}
.brand-tagline{left:240px;top:134px;font-size:23px;font-weight:700;color:var(--brand-dark)}
.head-contact{left:876px;top:124px;font-size:17px;font-weight:700;color:var(--teal);line-height:25px}
.head-contact svg{vertical-align:-2px;margin-right:8px}

.hero{left:0;top:184px;width:1200px;height:268px;background:linear-gradient(90deg,#0d3f6f,#134e84 60%,#0f4576)}
.hero-chevron{left:0;top:184px}
.hero-title{left:80px;top:236px;font-size:35px;font-weight:700;color:#fff;text-shadow:0 2px 3px rgba(0,0,0,.35)}
.hero-lead{left:80px;top:278px;font-size:20px;line-height:25px;color:#fff}
.btn{display:flex;align-items:center;height:31px;background:linear-gradient(#fff,#d8d8d8);border:1px solid #bbb;border-radius:2px;font-size:17px;font-weight:700;color:#333;top:357px}
.btn span.plus{width:26px;text-align:center;color:#777;border-right:1px solid #c8c8c8;margin-right:10px;font-weight:400}
.btn-more{left:82px;width:130px}
.btn-start{left:221px;width:190px}
.hero-photo{left:632px;top:184px;width:568px;height:268px;background:linear-gradient(90deg,#2b3440,#8c98a6 35%,#c9d2dc 70%,#e6ebf0)}

.intro-band{left:0;top:452px;width:1200px;height:242px;background:linear-gradient(#dde3ea,#fff 60%)}
.intro-title{left:74px;top:474px;font-size:27px;font-weight:700}
.intro-title em{font-style:normal;color:var(--brand-dark)}
.intro-list{left:74px;top:512px;list-style:none;font-size:16px;line-height:23px}
.intro-list li{padding-left:16px;position:relative}
.intro-list li::before{content:"";position:absolute;left:2px;top:6px;border:5px solid transparent;border-left:7px solid var(--blue-light);border-right:0}

.contact-card{left:768px;top:430px;width:336px;height:264px;background:#fff;box-shadow:0 4px 14px rgba(0,0,0,.18)}
.contact-tab{left:788px;top:430px;width:296px;height:42px;background:linear-gradient(#9a9a9a,#5e5e5e);border-radius:0 0 6px 6px;color:#fff;font-size:19px;font-weight:700;display:flex;align-items:center;padding-left:14px}
.contact-tab svg{margin-right:8px}
.contact-body{left:792px;top:490px;font-size:17px;line-height:19px}
.contact-body p{margin-bottom:18px}

.feature{width:330px;height:224px;top:724px;background:#fff;border:1px solid #e2e6ea;border-radius:8px 8px 0 0;box-shadow:0 2px 8px rgba(0,0,0,.08)}
.feature h3{height:48px;display:flex;align-items:center;padding-left:14px;font-size:17px;color:var(--teal);background:linear-gradient(#fff,#eef1f4);border-bottom:1px solid #dde2e7;border-radius:8px 8px 0 0}
.feature h3 svg{margin-right:8px}
.feature .notch{position:absolute;left:30px;top:48px;border:10px solid transparent;border-top-color:#e3e7eb;border-bottom:0}
.feature .copy{padding:24px 18px 0 27px;font-size:15.6px;line-height:19px;text-align:justify}
.feature .copy cite{font-weight:700;font-style:italic;display:block}
.f1{left:73px}.f2{left:424px}.f3{left:773px}
.btn-small{position:absolute;left:17px;top:178px;width:111px;height:24px;background:linear-gradient(#3d85c6,#1e5fa0);color:#fff;font-size:14px;border-radius:2px;display:flex;align-items:center;padding-left:13px}
.btn-small::after{content:"›";position:absolute;right:0;width:22px;text-align:center;border-left:1px solid #6da3d6}
.client-name{position:absolute;left:0;width:100%;top:110px;text-align:center;font-size:24px;font-weight:700;color:var(--blue-light)}
.client-name i{display:inline-block;width:16px;height:16px;background:var(--gold);margin-right:10px;vertical-align:0}

.site-footer{left:0;top:948px;width:1200px;height:71px;background:var(--navy);color:#fff}
.site-footer ul{list-style:none;display:flex;position:absolute;left:73px;top:18px;font-size:14px}
.site-footer li+li::before{content:"|";margin:0 7px}
.site-footer p{position:absolute;left:73px;top:40px;font-size:14px}
</style>
</head>
<body>
<nav class="abs top-nav">
  <ul><li>Home</li><li>Remote Backup</li><li>Emergency Services</li><li>Testimonials</li><li>Our Clients</li><li>About Us</li></ul>
  <span class="abs active-mark"></span>
</nav>

<header class="abs masthead"></header>
<div class="abs brand-mark"></div>
<div class="abs brand-name">Vaultrix</div>
<div class="abs brand-tagline">Keep Our Records</div>
<div class="abs head-contact">
  <div><svg width="16" height="12" viewBox="0 0 16 12"><path d="M1 4c4-4 10-4 14 0l-2 2-3-1V3H6v2L3 6z M3 7h10v5H3z" fill="#333"/></svg>+61 8 9000 4127</div>
  <div><svg width="16" height="12" viewBox="0 0 16 12"><rect width="16" height="12" fill="#333"/><path d="M0 0l8 6 8-6" stroke="#fff" fill="none"/></svg>service@vaultrix.net.au</div>
</div>

<section class="abs hero"></section>
<svg class="abs hero-chevron" width="640" height="268" viewBox="0 0 640 268"><path d="M0 0H510L600 120L555 268H0Z" fill="#1a5890" opacity=".45"/></svg>
<h1 class="abs hero-title">Vaultrix Computer Services</h1>
<p class="abs hero-lead">We keep your business records safe, always.<br>Backup your critical data off-site, every night.</p>
<div class="abs btn btn-more"><span class="plus">+</span>read more</div>
<div class="abs btn btn-start"><span class="plus">+</span>start backup now</div>
<div class="abs hero-photo" role="img" aria-label="Photograph of a professional woman standing in a server room"></div>

<section class="abs intro-band"></section>
<h2 class="abs intro-title"><em>Safe and Secure</em> your critical data</h2>
<ul class="abs intro-list">
  <li>Reliable backup is a vital part of risk management</li>
  <li>We keep your business records safe, always</li>
  <li>Database? Customer List? Financials? Contracts?</li>
  <li>Every hard disk fails one day</li>
  <li>We backup these valuable assets</li>
  <li>Critical data backup off-site, every night</li>
  <li>Located in Perth, Western Australia- the safest place on Earth</li>
</ul>

<aside class="abs contact-card"></aside>
<div class="abs contact-tab"><svg width="18" height="13" viewBox="0 0 18 13"><rect x=".5" y=".5" width="17" height="12" fill="none" stroke="#fff"/><path d="M1 1l8 6 8-6" stroke="#fff" fill="none"/></svg>Contact Now</div>
<div class="abs contact-body">
  <p>P.O.&nbsp; Box 418, South Perth,<br>Western Australia, 6951</p>
  <p><b>Telephone:</b><br>+61 8 9000 4127</p>
  <p><b>Email Information and Support:</b><br>service@vaultrix.net.au</p>
</div>

<article class="abs feature f1">
  <h3><svg width="16" height="16" viewBox="0 0 16 16"><rect x="1" y="1" width="14" height="14" fill="none" stroke="#333" stroke-width="2"/><path d="M1 5h14M6 5v10" stroke="#333" stroke-width="2"/></svg>Remote Backup</h3>
  <span class="notch"></span>
  <div class="copy">Vaultrix Computer Services operates secure Backup Servers at our WestIX Data Centre. Your system runs a program called a Backup Client on your File Server.</div>
  <span class="btn-small">read more</span>
</article>
<article class="abs feature f2">
  <h3><svg width="18" height="16" viewBox="0 0 18 16"><path d="M1 1h16v10H7l-4 4v-4H1z" fill="none" stroke="#333" stroke-width="2"/><path d="M4 5h10M4 8h7" stroke="#333"/></svg>Client Testimonials</h3>
  <span class="notch"></span>
  <div class="copy" style="text-align:left">"Graham you are a legend. We have an audit in progress today and I was able to illustrate a "Live" recovery. Thank you for service above and beyond the call of duty. We really appreciate that."<cite>Simon Harlow, Keystone Planning</cite></div>
</article>
<article class="abs feature f3">
  <h3><svg width="20" height="14" viewBox="0 0 20 14"><circle cx="7" cy="4" r="3.5" fill="#444"/><circle cx="14" cy="4" r="3" fill="#777"/><path d="M0 14c0-5 14-5 14 0zM10 9c4-2 10-1 10 5h-5z" fill="#555"/></svg>Our Customers</h3>
  <span class="notch"></span>
  <div class="client-name"><i></i>Harbourline Marine</div>
</article>

<footer class="abs site-footer">
  <ul><li>Home</li><li>Remote Backup</li><li>Emergency Services</li><li>Testimonials</li><li>Our Clients</li><li>About Us</li></ul>
  <p>Copyright © 2011 Vaultrix Computer Services. All Rights Reserved.</p>
</footer>
</body>
</html>
```